Spiritual journeyer, astrologer, Reiki master, underground music lover needs business card design

Initially I need a business card design (and possibly a logo for my new website). I offer astrological and energetic inquiry and guidance to clients in support of their life's evolutionary path. I combine an eclectic mix of methods with a focus on the mind body connection. I am a spiritual journeyer, astrologer, Reiki Master, certified personal trainer, soon to be black belt in Taekwondo (karate), and researcher into the benefits of music/sound vibrational therapy. And underground music lover :) The attached drawing is just something I drew freehand, it is symbolic of many things important to me. I wanted the figure to clearly be female. Her arms are open to catch the sky, the name of my new business is Orlabrook, and Orla is my daughter's name. This was just an idea I had, I'm open to suggestions. The photo is me with the planets in the sky as they were at the moment I was born (some years ago-LOL)
Updates

I have picked a final design. Thank you everyone for your time and effort.

Target Market(s)

Worldwide, what I do can be done in person or anywhere in the world via Skype

Industry/Entity Type

Professional Service

Contact Information for Business Card

Simple, unusual image with my business name and contact info

Font styles to use
Sans Serif

Requirements
Must have
• My website very clean, simple. Somehow combine biz name of Orlabrook with female figure catching/holding the starry sky? See my poor drawing I attached.
Nice to have
• Something that conveys all the unique, unusual, eclectic skills and capacities I have
Should not have
• Frilly, fancy, stuffy

```html
<!DOCTYPE html>
<html lang="en">
<head>
<meta charset="utf-8">
<title>Orlabrook – Business Card</title>
<link href="https://fonts.googleapis.com/css2?family=Jost:wght@400&family=Karla:wght@400&family=Lora:ital@1&display=swap" rel="stylesheet">
<style>
  :root {
    --backdrop: #2c2c2c;
    --card: #ffffff;
    --indigo: #2a1a6e;
    --amber: #e07a1f;
    --ink: #1f1f1f;
    --photo-warm: #c0392b;
    --photo-deep: #5a2a1e;
    --photo-light: #e9d9c4;
  }
  html, body {
    margin: 0;
    width: 1200px;
    height: 1200px;
    overflow: hidden;
    background: var(--backdrop);
  }
  .canvas {
    position: relative;
    width: 1200px;
    height: 1200px;
  }
  .business-card {
    position: absolute;
    left: 100px;
    top: 310px;
    width: 1000px;
    height: 580px;
    background: var(--card);
    box-shadow: 0 12px 30px rgba(0,0,0,0.45);
  }
  .brand-name {
    position: absolute;
    left: 78px;
    top: 62px;
    margin: 0;
    font-family: "Jost", sans-serif;
    font-weight: 400;
    font-size: 60px;
    letter-spacing: 0.56em;
    color: var(--indigo);
    line-height: 1;
  }
  .owner-name {
    position: absolute;
    left: 88px;
    top: 190px;
    margin: 0;
    font-family: "Lora", serif;
    font-style: italic;
    font-size: 33px;
    color: var(--amber);
  }
  .service-line {
    position: absolute;
    left: 92px;
    top: 285px;
    margin: 0;
    font-family: "Karla", sans-serif;
    font-size: 25px;
    line-height: 1.3;
    color: var(--ink);
  }
  .contact-list {
    position: absolute;
    left: 104px;
    top: 410px;
    margin: 0;
    padding: 0;
    list-style: none;
    font-family: "Karla", sans-serif;
    font-size: 25px;
    line-height: 1.32;
    color: var(--ink);
  }
  .portrait {
    position: absolute;
    left: 790px;
    top: 205px;
    width: 178px;
    height: 222px;
    background: linear-gradient(160deg, var(--photo-light) 0%, var(--photo-warm) 55%, var(--photo-deep) 100%);
  }
</style>
</head>
<body>
  <main class="canvas">
    <section class="business-card">
      <h1 class="brand-name">ORLABROOK</h1>
      <p class="owner-name">Maren Ellison</p>
      <p class="service-line">Astrological and Energetic<br>Guidance Inquiry</p>
      <ul class="contact-list">
        <li>www.orlabrook.com</li>
        <li>hello@orlabrook.com</li>
        <li>555-014-2297</li>
      </ul>
      <div class="portrait" role="img" aria-label="Portrait photograph of the astrologer in a red blouse"></div>
    </section>
  </main>
</body>
</html>
```